New clean and fresh corporate PPT template for Telecom equipment maker

KRV (BORVEX KRVT) is a telecom equipment maker in Silicon Valley. Our current PPT template that goes with http://melikport.com is overbuilt, dark, huge in file size, and looks the opposite of fresh and clean.
Our new microsite @ http://investor-krvt.com is the direction we want to go. We are B2B, selling to telecom operators, but still want something that looks clean and fresh and not stuffy, hence primarily white background with maximum whitespace in 16:9 format.
Style guidelines attached, exclusive use of approved colors required, the master should remain as simple as possible, and we want the file size to stay reasonable (i.e. less is better). Features we would like include:
- Lato font built-in to the template
- Text boxes with standard size fonts, that automatically get smaller with indention
- An interesting bullet style, nothing crazy, but with visual interest
- A pre-selected table format that is clean and allows for high-density tables with many rows & columns
- Whichever standard slides layouts in the master you think would help result in slides that are found in the current deck, without someone needing to build their own slide

```html
<!DOCTYPE html>
<html lang="en">
<head>
<meta charset="utf-8">
<title>Passive Optical LAN (POL) Versus Legacy Copper LAN</title>
<link href="https://fonts.googleapis.com/css2?family=Lato:ital,wght@0,400;0,700;1,400&family=Titillium+Web:wght@400;600&display=swap" rel="stylesheet">
<style>
  :root {
    --slate: #4b5b70;
    --ink: #2e2e33;
    --navy-italic: #1f3f8f;
    --muted: #7a7a80;
    --teal: #3cc8c8;
    --lime: #8cd200;
    --coral: #f25c5c;
    --axis: #c9c9cc;
    --seg-vertical: #e3e3e5;
    --seg-horizontal: #c4c3cb;
    --seg-passive: #8e8d9b;
    --seg-network: #0d5aa7;
    --seg-endpoint: #050a2a;
    --seg-training: #f7a11d;
    --seg-fault: #474a5e;
    --seg-testing: #6cbd45;
    --seg-capacity: #2ec5ef;
    --seg-floor: #e8194f;
  }
  html, body { margin: 0; padding: 0; overflow: hidden; background: #fff; }
  .slide {
    position: relative; width: 1200px; height: 675px; overflow: hidden;
    background: #fff; font-family: "Lato", sans-serif; color: var(--ink);
  }
  .slide-title {
    position: absolute; left: 0; width: 1200px; top: 34px; margin: 0;
    text-align: center; font-size: 44px; font-weight: 400; color: var(--slate);
    letter-spacing: -0.3px;
  }
  .title-rule { position: absolute; left: 537px; top: 101px; display: flex; height: 4px; }
  .title-rule span { width: 42px; height: 4px; }
  .title-rule .teal { background: var(--teal); }
  .title-rule .lime { background: var(--lime); }
  .title-rule .coral { background: var(--coral); }

  .case-tagline {
    position: absolute; left: 60px; width: 430px; top: 132px; margin: 0;
    text-align: center; font-style: italic; font-size: 20px; line-height: 24px;
    color: var(--navy-italic); letter-spacing: -0.4px;
  }
  .advantages { position: absolute; left: 42px; top: 224px; width: 480px; }
  .advantage-head { margin: 0; font-size: 19.5px; line-height: 24px; letter-spacing: -0.3px; }
  .advantage-items { margin: 6px 0 8px 28px; font-size: 19.5px; line-height: 24px; letter-spacing: -0.2px; }

  .chart { position: absolute; left: 580px; width: 600px; font-family: "Titillium Web", sans-serif; }
  .chart text { font-family: "Titillium Web", sans-serif; }

  .footer-note {
    position: absolute; left: 0; width: 1160px; top: 643px; text-align: center;
    font-size: 14px; color: var(--muted);
  }
  .page-number { position: absolute; left: 1128px; top: 634px; font-size: 19px; color: var(--slate); }
  .page-rule { position: absolute; left: 1126px; top: 623px; width: 74px; height: 4px; background: var(--teal); }
  .brand { position: absolute; left: 16px; top: 620px; display: flex; align-items: center; gap: 8px; }
  .brand-mark { width: 14px; height: 14px; background: var(--teal); }
  .brand-name { font-size: 30px; font-weight: 700; color: #a9abb0; letter-spacing: 1px; }
</style>
</head>
<body>
<div class="slide">
  <h1 class="slide-title">Passive Optical LAN (POL) Versus Legacy Copper LAN</h1>
  <div class="title-rule"><span class="teal"></span><span class="lime"></span><span class="coral"></span></div>

  <p class="case-tagline">POL Business case: Modernize a 30 year old Enterprise Copper Networking Architecture</p>

  <div class="advantages">
    <p class="advantage-head">POL CAPEX Advantage of 61% Savings versus Legacy<br>LAN</p>
    <p class="advantage-items">• New Cabling and Installs • Equipment Costs</p>
    <p class="advantage-head">POL OPEX Advantage of 54% Savings versus Legacy<br>LAN</p>
    <p class="advantage-items">• Power • Floor space • Service contracts • Fault<br>management • Testing and certification •<br>Capacity management • Network<br>upgrades/patches • Preventive maintenance •<br>Training. • Eco-Friendly - Green</p>
    <p class="advantage-head">POL TCO Advantage of 58% Savings versus Legacy<br>LAN</p>
    <p class="advantage-items">• Bandwidth Future Proof • SDN and NFV Ready</p>
  </div>

  <svg class="chart" style="top:115px" width="600" height="220" viewBox="580 115 600 220" role="img" aria-label="CAPEX comparison bar chart, 61% savings">
    <g font-size="9" fill="#333" text-anchor="middle">
      <text x="594" y="285">0</text><text x="594" y="259">1</text><text x="594" y="234">2</text>
      <text x="594" y="208">3</text><text x="594" y="182">4</text><text x="594" y="156">5</text><text x="594" y="130">6</text>
    </g>
    <line x1="603" y1="282.5" x2="1152" y2="282.5" stroke="var(--axis)" stroke-width="1.5"/>
    <rect x="690" y="185" width="64" height="97" fill="var(--seg-horizontal)"/>
    <rect x="690" y="146" width="64" height="39" fill="var(--seg-network)"/>
    <rect x="967" y="266" width="63" height="16" fill="var(--seg-horizontal)"/>
    <rect x="967" y="261" width="63" height="5" fill="var(--seg-passive)"/>
    <rect x="967" y="252" width="63" height="9" fill="var(--seg-network)"/>
    <rect x="967" y="228" width="63" height="24" fill="var(--seg-endpoint)"/>
    <line x1="758" y1="146" x2="961" y2="228.5" stroke="#555" stroke-width="0.8"/>
    <path d="M955 224 L962 229 L954 229" fill="none" stroke="#555" stroke-width="0.8"/>
    <text x="861" y="174" font-size="9" font-weight="600" text-anchor="middle" fill="#222">61%</text>
    <g font-size="9.5" fill="#333" text-anchor="middle">
      <text x="720" y="297">AE</text><text x="998" y="297">POL</text>
    </g>
    <g font-size="10" fill="#444">
      <rect x="603" y="315" width="12" height="12" fill="var(--seg-vertical)"/><text x="621" y="325">Vertical cabling</text>
      <rect x="704" y="315" width="12" height="12" fill="var(--seg-horizontal)"/><text x="724" y="325">Horizontal cabling</text>
      <rect x="819" y="315" width="12" height="12" fill="var(--seg-passive)"/><text x="837" y="325">Passive</text>
      <rect x="891" y="315" width="12" height="12" fill="var(--seg-network)"/><text x="909" y="325">Network electronics</text>
      <rect x="1012" y="315" width="12" height="12" fill="var(--seg-endpoint)"/><text x="1030" y="325">Endpoint electronics</text>
    </g>
  </svg>

  <svg class="chart" style="top:350px" width="600" height="250" viewBox="580 350 600 250" role="img" aria-label="OPEX comparison bar chart, 54% savings">
    <g font-size="9" fill="#333" text-anchor="middle">
      <text x="594" y="517">0</text><text x="594" y="492">1</text><text x="594" y="466">2</text>
      <text x="594" y="440">3</text><text x="594" y="414">4</text><text x="594" y="389">5</text><text x="594" y="363">6</text>
    </g>
    <line x1="603" y1="514.5" x2="1159" y2="514.5" stroke="var(--axis)" stroke-width="1.5"/>
    <rect x="714" y="503" width="66" height="11" fill="var(--seg-network)"/>
    <rect x="714" y="497.5" width="66" height="5.5" fill="var(--seg-floor)"/>
    <rect x="714" y="480" width="66" height="17.5" fill="var(--seg-horizontal)"/>
    <rect x="714" y="455" width="66" height="25" fill="var(--seg-fault)"/>
    <rect x="714" y="449" width="66" height="6" fill="var(--seg-testing)"/>
    <rect x="714" y="434" width="66" height="15" fill="var(--seg-capacity)"/>
    <rect x="714" y="414" width="66" height="20" fill="var(--seg-vertical)"/>
    <rect x="714" y="412.5" width="66" height="1.5" fill="var(--seg-passive)"/>
    <rect x="714" y="407" width="66" height="5.5" fill="var(--seg-training)"/>
    <rect x="977" y="508" width="66" height="6" fill="var(--seg-network)"/>
    <rect x="977" y="505" width="66" height="3" fill="var(--seg-floor)"/>
    <rect x="977" y="499" width="66" height="6" fill="var(--seg-horizontal)"/>
    <rect x="977" y="486" width="66" height="13" fill="var(--seg-fault)"/>
    <rect x="977" y="480" width="66" height="6" fill="var(--seg-testing)"/>
    <rect x="977" y="475" width="66" height="5" fill="var(--seg-capacity)"/>
    <rect x="977" y="470" width="66" height="5" fill="var(--seg-vertical)"/>
    <rect x="977" y="464" width="66" height="6" fill="var(--seg-training)"/>
    <line x1="784" y1="408" x2="973" y2="464" stroke="#555" stroke-width="0.8"/>
    <path d="M967 460 L974 464 L966 466" fill="none" stroke="#555" stroke-width="0.8"/>
    <text x="884" y="427" font-size="9" font-weight="600" text-anchor="middle" fill="#222">54%</text>
    <g font-size="9.5" fill="#333" text-anchor="middle">
      <text x="745" y="529">AE</text><text x="1009" y="529">POL</text>
    </g>
    <g font-size="10" fill="#444">
      <rect x="603" y="546" width="12" height="12" fill="var(--seg-vertical)"/><text x="621" y="556">Network upgrades/patches</text>
      <rect x="603" y="565" width="12" height="12" fill="var(--seg-fault)"/><text x="621" y="575">Fault management</text>
      <rect x="603" y="583" width="12" height="12" fill="var(--seg-network)"/><text x="621" y="593">Power</text>
      <rect x="758" y="546" width="12" height="12" fill="var(--seg-passive)"/><text x="776" y="556">Preventive maintenance</text>
      <rect x="758" y="565" width="12" height="12" fill="var(--seg-testing)"/><text x="776" y="575">Testing and certification</text>
      <rect x="758" y="583" width="12" height="12" fill="var(--seg-floor)"/><text x="776" y="593">Floor space</text>
      <rect x="907" y="546" width="12" height="12" fill="var(--seg-training)"/><text x="925" y="556">Training</text>
      <rect x="907" y="565" width="12" height="12" fill="var(--seg-capacity)"/><text x="925" y="575">Capacity management</text>
      <rect x="907" y="583" width="12" height="12" fill="var(--seg-horizontal)"/><text x="925" y="593">Service contracts</text>
    </g>
  </svg>

  <div class="brand"><span class="brand-mark"></span><span class="brand-name">KRV</span></div>
  <div class="footer-note">© 2018 Korvel Reach Systems – Proprietary and Confidential</div>
  <div class="page-rule"></div>
  <div class="page-number">20</div>
</div>
</body>
</html>
```